Floorplan brochure design for rental company

We need a brochure designed for our rental company, Birch Hollow Commons.
We have two different categories that we need on this brochure: townhomes (primary) and mobile homes. Size and layout is up to you... choose what you think works best for the information being presented. However, please do not use an odd shape or size; do use a size and format that can be printed by printvexa.com.
Font and color choices are up to you. If needed, the fonts from the logo are Americana Extra Bold and BlackJack.
Industry/Entity Type
It Company
Requirements
Must have
- 1. logo and office address/contact information
2. floorplans and prices from attached documents
3. amenities from attached document
Should not have
- Please do not use our website, birchhollow.com, as a basis for any design or color scheme decisions. We are working on a redesign of that website with our new logo (attached).

```html
<!DOCTYPE html>
<html lang="en">
<head>
<meta charset="utf-8">
<title>Birch Hollow Commons – Floorplan Brochure</title>
<link rel="stylesheet" href="https://fonts.googleapis.com/css2?family=Barlow+Semi+Condensed:wght@400;500;600;700&display=swap">
<style>
  :root {
    --green: #2f9a47;
    --blue: #1f9dc8;
    --ink: #2a2a2a;
    --page-line: #b9b9b9;
    --plan-fill: #ededed;
    --plan-edge: #4a4a4a;
    --rule: #c9c9c9;
    --white: #ffffff;
  }
  * { box-sizing: border-box; margin: 0; padding: 0; }
  html, body { width: 1200px; height: 1200px; overflow: hidden; background: var(--white); }
  body { position: relative; font-family: "Barlow Semi Condensed", "Arial Narrow", sans-serif; color: var(--ink); }

  .page { position: absolute; top: 234px; width: 529px; height: 685px; border: 1px solid var(--page-line); background: var(--white); }
  .page--cover { left: 56px; }
  .page--plans { left: 623px; }

  .brand { position: absolute; display: flex; align-items: center; gap: 8px; color: var(--green); font-weight: 700; line-height: 1.05; }
  .brand__dot { width: 14px; height: 14px; border-radius: 50%; background: var(--green); flex: none; }
  .page--cover .brand { left: 34px; top: 72px; font-size: 21px; width: 150px; }
  .page--plans .brand { left: 418px; top: 570px; font-size: 15px; width: 108px; }

  .category-band { position: absolute; left: 100px; width: 429px; height: 33px; border-radius: 5px 0 0 5px; color: var(--white); font-weight: 700; font-size: 20px; line-height: 33px; padding-left: 16px; }
  .category-band--townhomes { top: 191px; background: var(--green); }
  .category-band--mobile { top: 227px; background: var(--blue); }

  .amenities { position: absolute; left: 115px; top: 280px; width: 400px; }
  .amenities__title { color: var(--green); font-size: 17px; font-weight: 700; margin-bottom: 2px; }
  .amenities__cols { display: flex; }
  .amenities__col { width: 168px; font-size: 11.5px; line-height: 15.6px; }
  .amenities__col + .amenities__col { width: 200px; }
  .amenities h3 { font-size: 12px; font-weight: 700; line-height: 15.6px; }
  .amenities h3.spaced { margin-top: 14px; }
  .amenities ul { list-style: none; }
  .amenities li { padding-left: 8px; text-indent: -8px; }
  .amenities li::before { content: "• "; }
  .amenities .footnote { font-size: 8px; margin-top: 3px; }

  .info-box { position: absolute; left: 100px; top: 548px; width: 429px; height: 103px; background: var(--green); border-radius: 5px 0 0 5px; color: var(--white); padding: 12px 16px; }
  .info-box h2 { font-size: 16px; font-weight: 700; margin-bottom: 6px; }
  .info-box p { font-size: 12.5px; line-height: 16px; }

  .section-title { position: absolute; left: 28px; font-size: 20px; font-weight: 700; }
  .section-title--townhomes { top: 30px; color: var(--green); }
  .section-title--mobile { top: 274px; color: var(--blue); }

  .plan { position: absolute; }
  .plan__num { position: absolute; left: -1px; top: -2px; font-size: 11px; font-weight: 700; }
  .plan__drawing { position: absolute; background: var(--plan-fill); border: 1.5px solid var(--plan-edge); }

  .price-list { position: absolute; left: 28px; font-size: 10px; line-height: 12.2px; list-style: none; }
  .price-list li { display: flex; }
  .price-list .label { width: 58px; color: var(--green); font-weight: 700; font-size: 11px; }
  .price-list .price { width: 38px; color: var(--green); font-weight: 700; font-size: 11px; }
  .price-list--townhomes { top: 183px; }
  .price-list--mobile { top: 566px; }
  .price-list--mobile .label, .price-list--mobile .price { color: var(--blue); }

  .divider { position: absolute; left: 28px; top: 259px; width: 472px; height: 1px; background: var(--rule); }
</style>
</head>
<body>

<section class="page page--cover">
  <div class="brand"><span class="brand__dot"></span>Birch Hollow Commons</div>

  <div class="category-band category-band--townhomes">Townhomes</div>
  <div class="category-band category-band--mobile">Mobile homes</div>

  <div class="amenities">
    <h2 class="amenities__title">Amenities</h2>
    <div class="amenities__cols">
      <div class="amenities__col">
        <h3>Overall features:</h3>
        <ul>
          <li>Golf course</li>
          <li>Convenience store</li>
          <li>Gated access</li>
          <li>Playground</li>
          <li>Basketball courts</li>
          <li>Stocked fishing lake</li>
          <li>Pet friendly*</li>
          <li>Dog park</li>
          <li>Extra storage available</li>
          <li>Lawn care included</li>
          <li>Outdoor grills permitted</li>
        </ul>
        <p class="footnote">*breed restrictions</p>
      </div>
      <div class="amenities__col">
        <h3>Townhomes:</h3>
        <ul>
          <li>6 Foot privacy fenced backyard</li>
          <li>Concrete backyard patio</li>
          <li>Assigned front door parking</li>
          <li>Ceiling fans in every room</li>
          <li>Dishwasher, microwave, refrigerator and range</li>
          <li>Full size washer and dryer connections</li>
        </ul>
        <h3 class="spaced">Mobile homes:</h3>
        <ul>
          <li>Large fenced backyards</li>
          <li>Concrete patio</li>
          <li>Private driveway</li>
        </ul>
      </div>
    </div>
  </div>

  <div class="info-box">
    <h2>For more information</h2>
    <p>Call 281-555-0148</p>
    <p>Visit www.birchhollow.com</p>
    <p>Or call by our office at 1180 Alder Lane, Fairhaven, TX, 77411</p>
  </div>
</section>

<section class="page page--plans">
  <h2 class="section-title section-title--townhomes">Townhomes</h2>

  <div class="plan" style="left:26px;top:62px;">
    <span class="plan__num">1</span>
    <div class="plan__drawing" role="img" aria-label="Floorplan 1: two-storey townhome, bedrooms upstairs, kitchen, dining and living room downstairs" style="left:10px;top:4px;width:154px;height:114px;"></div>
  </div>
  <div class="plan" style="left:194px;top:62px;">
    <span class="plan__num">2</span>
    <div class="plan__drawing" role="img" aria-label="Floorplan 2: two-storey townhome, two bedrooms upstairs, kitchen, dining and living room downstairs" style="left:10px;top:4px;width:148px;height:114px;"></div>
  </div>
  <div class="plan" style="left:370px;top:62px;">
    <span class="plan__num">3</span>
    <div class="plan__drawing" role="img" aria-label="Floorplan 3: single-level townhome with master suite, second bedroom, kitchen, dining and living room" style="left:10px;top:4px;width:112px;height:144px;"></div>
  </div>

  <ul class="price-list price-list--townhomes">
    <li><span class="label">1.&nbsp; Plan 1132</span><span class="price">$875</span><span>2 br, 2.5 bath, 2 storey</span></li>
    <li><span class="label">2.&nbsp; Plan 1272</span><span class="price">$925</span><span>2 br, 2.5 bath, 2 storey</span></li>
    <li><span class="label">3.&nbsp; Plan 1069</span><span class="price">$900</span><span>2 br, 2 bath</span></li>
    <li><span class="label">&nbsp;&nbsp;&nbsp;&nbsp; Plan 1070</span><span class="price">$925</span><span>2 br, 2 bath, covered patio</span></li>
  </ul>

  <div class="divider"></div>

  <h2 class="section-title section-title--mobile">Mobile homes</h2>

  <div class="plan" style="left:26px;top:310px;">
    <span class="plan__num">4</span>
    <div class="plan__drawing" role="img" aria-label="Floorplan 4: 16 by 76 mobile home, three bedrooms, two baths" style="left:10px;top:2px;width:288px;height:60px;"></div>
  </div>
  <div class="plan" style="left:26px;top:386px;">
    <span class="plan__num">5</span>
    <div class="plan__drawing" role="img" aria-label="Floorplan 5: 16 by 76 mobile home, three bedrooms, two baths" style="left:10px;top:4px;width:288px;height:62px;"></div>
  </div>
  <div class="plan" style="left:26px;top:472px;">
    <span class="plan__num">6</span>
    <div class="plan__drawing" role="img" aria-label="Floorplan 6: 16 by 52 mobile home, two bedrooms, one bath" style="left:10px;top:2px;width:214px;height:70px;"></div>
  </div>
  <div class="plan" style="left:276px;top:474px;">
    <span class="plan__num">7</span>
    <div class="plan__drawing" role="img" aria-label="Floorplan 7: 11 by 35 studio mobile home with bedroom, kitchen, dining and living room" style="left:14px;top:0;width:180px;height:70px;border-width:2.5px;"></div>
  </div>

  <ul class="price-list price-list--mobile">
    <li><span class="label">4.&nbsp; Plan 1887</span><span class="price">$875</span><span>16' x 76' 3br, 2 bath</span></li>
    <li><span class="label"></span><span class="price">$950</span><span>16' x 76' 3br, 2 bath, with 8' x 8' storage bldg</span></li>
    <li><span class="label">5.&nbsp; Plan 2762</span><span class="price">$850</span><span>16' x 76' 3br, 2 bath</span></li>
    <li><span class="label">6.&nbsp; Plan 1648</span><span class="price">$750</span><span>16' x 52' 2br, 1 bath</span></li>
    <li><span class="label">7.&nbsp; Plan 105</span><span class="price">$1050</span><span>11' x 35' 1br, 1 bath, furnished including utilities</span></li>
  </ul>

  <div class="brand"><span class="brand__dot"></span>Birch Hollow Commons</div>
</section>

</body>
</html>
```